EPIC, awesome, creative business card needed - get involved!

I'm launching a boutique, exclusive Property Management real estate agency in Sydney early next year.
The name of the agency will be called "Quartz Hill Lane" - it's a play on "chase the silver pebble trail" to wealth. The Quartz Hill Lane signifies wealth through property investment.
My business will offer management of investment properties (ie Property Management).
The difference with Quartz Hill Lane and other agencies is the business will be run by one of Australia's leading property investment experts, and also one of Australia's leading property managers.
It will be exclusively for high net worth properties and individuals, so the business card needs to be extremely sharp, slick and relatively simple.
The information I want on the card is as follows
Nolan Pryce - Director
M: 0412 967 154
P: 9735 6021
E: nolan@quartzhilllane.net.au
W: quartzhilllane.net.au
I'm happy with the red from the logo, black - no yellows or funky colors. I want this to be a super corporate and slick business card to match the high end nature of the business.
Good luck everyone, and please ask questions for clarification.

```html
<!DOCTYPE html>
<html lang="en">
<head>
<meta charset="utf-8">
<title>Quartz Hill Lane – Business Card</title>
<link rel="stylesheet" href="https://fonts.googleapis.com/css2?family=Oswald:wght@600&display=swap">
<style>
  :root {
    --page: #ffffff;
    --card: #000000;
    --brand-red: #c00000;
    --ink-light: #ffffff;
  }
  * { box-sizing: border-box; margin: 0; padding: 0; }
  html, body {
    width: 1200px; height: 360px; overflow: hidden;
    background: var(--page);
  }
  .canvas { position: relative; width: 1200px; height: 360px; }

  .card {
    position: absolute; top: 17px;
    width: 553px; height: 327px;
    background: var(--card);
    overflow: hidden;
  }
  .card--front { left: 17px; }
  .card--back  { left: 630px; }

  .rule { position: absolute; background: var(--brand-red); }

  .wordmark {
    position: absolute;
    display: flex; align-items: center; gap: 6px;
    font-family: "Oswald", sans-serif; font-weight: 600;
    color: var(--ink-light);
    white-space: nowrap;
    font-size: 17px; line-height: 22px;
  }
  .wordmark__square {
    width: 14px; height: 14px;
    background: var(--brand-red); flex: none;
  }

  .card--front .wordmark { left: 40px; top: 40px; }
  .card--back .wordmark  { left: 20px; top: 60px; }

  .contact {
    position: absolute; left: 184px; top: 167px;
    width: 365px; height: 118px;
    background: var(--brand-red);
    padding: 13px 0 0 10px;
    font-family: "Oswald", sans-serif; font-weight: 600;
    color: var(--ink-light); font-size: 14.5px; line-height: 18.5px;
    list-style: none;
  }
  .contact__name { font-size: 15px; }
  .contact__role { font-size: 10px; }
</style>
</head>
<body>
<main class="canvas">

  <section class="card card--front" aria-label="Card front">
    <div class="wordmark">
      <span class="wordmark__square"></span>
      <span class="wordmark__name">Quartz Hill Lane</span>
    </div>
    <span class="rule" style="left:150px; top:99px; width:6px; height:228px;"></span>
    <span class="rule" style="left:116px; top:150px; width:330px; height:6px;"></span>
    <ul class="contact">
      <li><span class="contact__name">Nolan Pryce</span> - <span class="contact__role">Director</span></li>
      <li>M: 0412 967 154</li>
      <li>P: 9735 6021</li>
      <li>E: nolan@quartzhilllane.net.au</li>
      <li>W: quartzhilllane.net.au</li>
    </ul>
  </section>

  <section class="card card--back" aria-label="Card back">
    <div class="wordmark">
      <span class="wordmark__square"></span>
      <span class="wordmark__name">Quartz Hill Lane</span>
    </div>
    <span class="rule" style="left:176px; top:0; width:6px; height:272px;"></span>
    <span class="rule" style="left:46px; top:212px; width:391px; height:6px;"></span>
  </section>

</main>
</body>
</html>
```